Redesign of a Reputation Management Website

StandingMend.com Requirement Doc
Reference Site: NameHarbor.com (should NOT copy this site but be patterned in a similar way because we are changing the back end and functionality similar to it)
StandingMend.com is a functional active site that needs a redesign.
FRONT END
Landing / Home Page:
• Should be built with WordPress for ease of use
• Should contain high quality imagery
• Should contain logo
• Should contain Navigation links on top right or top center
1. Personal
2. Business
3. About us
4. Account Login
5. Sign Up
• Should be broken into sections
1. Header – High Quality Image/Slider/Social Media Icons/Contact Info
2. Information
3. Services Personal / Business
4. Sign Up
5. Footer – Links/Contacts/ Social media
6. Sub footer- Info Links
Landing / Home Page Colours:
Main colours should be contrasting light and dark blues like #1A9BFC, #31A5FC and #60BAF7, with minimal green like #77AE00 as an accent colour. The footer and sub footer should be #1C3344
Landing / Home Functional Requirements:
All front end links should link out their individual pages and/or back end processes, this includes navigation menu items, footer links, and sign up and social media buttons. All linked pages should contain I quality information, Graphics, calls to action and sign up options.
Sign up should have two options, Sign up with social media accounts or standard sign up form.
Login should have two options, Login with social media accounts or standard login form.
Target Market(s)
People that are looking to manage their reputation or repair it, or manage their brand, monitor their reputation online
Industry/Entity Type
Management
Number of Pages Required
1 page
Look and feel

```html
<!DOCTYPE html>
<html lang="en">
<head>
<meta charset="utf-8">
<title>Standing Mend – Reputation Consulting</title>
<link href="https://fonts.googleapis.com/css2?family=Raleway:wght@400;500;600&family=Open+Sans:wght@400;600;700&display=swap" rel="stylesheet">
<style>
:root{
  --blue:#1a82f0;
  --blue-light:#31a5fc;
  --blue-pale:#60baf7;
  --green:#77ae00;
  --ink:#1f2a33;
  --text:#5b6670;
  --footer:#1c3344;
  --footer-deep:#14232f;
  --footer-text:#8795a1;
  --white:#fff;
}
*{margin:0;padding:0;box-sizing:border-box}
html,body{width:705px;height:1200px;overflow:hidden;background:var(--white)}
body{position:relative;font-family:"Open Sans",sans-serif;color:var(--text)}
.abs{position:absolute}
.raleway{font-family:"Raleway",sans-serif}

/* header */
.brand{left:110px;top:17px;display:flex;align-items:center;gap:6px}
.brand-mark{width:22px;height:22px;border-radius:50%;background:var(--blue)}
.brand-name{font-family:"Open Sans",sans-serif;font-weight:700;font-size:15px;color:var(--ink);line-height:1}
.brand-tag{left:138px;top:39px;font-size:6.5px;color:#7b868f}
.contact-top{right:106px;top:13px;text-align:right;font-size:6.4px;line-height:12.5px;color:#4b5660}
.contact-line{right:106px;top:38px;display:flex;align-items:center;gap:5px;font-size:7px;color:#4b5660}
.social{display:flex;gap:5px}
.social span{width:9px;height:9px;border-radius:50%;background:#5a7189;display:block}
.icon-green{fill:var(--green)}

.nav{left:0;top:58px;width:705px;height:28px;background:linear-gradient(var(--blue-light),var(--blue))}
.nav a{position:absolute;top:0;height:28px;line-height:28px;color:var(--white);font-family:"Raleway",sans-serif;font-size:9.5px;text-decoration:none;transform:translateX(-50%)}
.nav .sep{position:absolute;top:0;width:1px;height:28px;background:rgba(255,255,255,.35)}

/* hero */
.hero{left:0;top:86px;width:705px;height:271px;background:linear-gradient(90deg,#f4f8fc 0%,#e6eef6 35%,#c9d8e6 55%,#8fa6bd 75%,#dfe7ee 100%)}
.hero-title{left:108px;top:153px;font-family:"Raleway",sans-serif;font-size:25px;color:var(--blue);font-weight:400}
.hero-sub{left:108px;top:185px;font-family:"Raleway",sans-serif;font-size:14px;color:var(--ink)}
.hero-text{left:108px;top:209px;width:200px;font-size:6.8px;line-height:12px;color:#4b5660}
.dots{left:110px;top:242px;display:flex;gap:3px}
.dots span{width:8px;height:8px;border-radius:50%;background:#a8b3bc}
.dots span:first-child{background:var(--ink)}

/* welcome */
.welcome-title{left:0;top:392px;width:705px;text-align:center;font-family:"Raleway",sans-serif;font-size:18.5px;color:var(--blue)}
.welcome-text{left:125px;top:424px;width:455px;text-align:center;font-size:6.4px;line-height:12.8px}
.welcome-text p+p{margin-top:4px}

/* services */
.services{left:0;top:525px;width:705px;height:271px;background:linear-gradient(#ececec,#fff 30%)}
.services-title{left:0;top:561px;width:705px;text-align:center;font-family:"Raleway",sans-serif;font-size:16.5px;color:var(--ink)}
.service{top:612px;width:120px;text-align:center}
.service svg{display:block;margin:0 auto 15px}
.service h3{font-family:"Raleway",sans-serif;font-weight:500;font-size:9.2px;line-height:12px;color:var(--ink);margin-bottom:7px}
.service p{font-size:5.6px;line-height:10.4px}
.service a{display:block;margin-top:7px;font-size:6.2px;font-weight:700;color:var(--blue);text-decoration:none}
.arrow{top:652px}

/* signup */
.signup{left:0;top:796px;width:705px;height:206px;background:var(--blue)}
.signup-photo{left:440px;top:803px;width:125px;height:199px;border-radius:60px 60px 0 0;background:linear-gradient(#e7d8c8,#b8d0ef 45%,#9ebfe8)}
.signup-title{left:118px;top:833px;font-family:"Raleway",sans-serif;font-size:16px;color:var(--white)}
.signup-text{left:118px;top:857px;width:280px;font-size:5.8px;line-height:10px;color:var(--blue-pale)}
.field{width:106px;height:16px;background:linear-gradient(#fff,#eee);border:1px solid #d9d9d9;font-size:5.6px;line-height:14px;padding-left:7px;color:#666}
.btn{top:934px;height:20px;font-size:7.5px;font-weight:600;color:var(--white);display:flex;align-items:center;justify-content:center;gap:5px}
.btn-green{left:118px;width:64px;background:var(--green);border:1px solid #fff}
.btn-social{left:212px;width:81px;border:1px solid #fff}
.btn-social i{width:6px;height:9px;background:#fff;display:block}
.or{left:193px;top:938px;font-size:9px;color:var(--white)}

/* footer */
.footer{left:0;top:1002px;width:705px;height:163px;background:var(--footer)}
.col{top:1029px}
.col h4{font-family:"Raleway",sans-serif;font-weight:500;font-size:9px;color:var(--white);margin-bottom:6px}
.col li{list-style:none;font-size:6.5px;line-height:13.7px;color:var(--footer-text)}
.col li b{font-weight:400;color:var(--white)}
.col-rule{top:1035px;width:1px;height:98px;background:#2a4255}
.footer-social{left:483px;top:1121px;display:flex;gap:6px}
.footer-social span{width:10px;height:10px;border-radius:50%;background:var(--white)}
.subfooter{left:0;top:1165px;width:705px;height:35px;background:var(--footer-deep)}
.subfooter p{position:absolute;left:111px;top:13px;font-size:5.6px;color:var(--footer-text)}
</style>
</head>
<body>

<header>
  <div class="abs brand"><span class="brand-mark"></span><span class="brand-name">Standing Mend</span></div>
  <div class="abs brand-tag">Reputation Consulting Since 1992</div>
  <div class="abs contact-top">
    <svg width="6" height="8" viewBox="0 0 6 8"><path class="icon-green" d="M3 0a3 3 0 0 0-3 3c0 2 3 5 3 5s3-3 3-5a3 3 0 0 0-3-3zm0 4a1 1 0 1 1 0-2 1 1 0 0 1 0 2z"/></svg>
    12-480 Larkmoor Avenue, Suite 210,<br>Fernvale, Ontario, Canada K0F 2B9
  </div>
  <div class="abs contact-line">
    <div class="social"><span></span><span></span><span></span><span></span></div>
    <svg width="7" height="7" viewBox="0 0 10 10"><path class="icon-green" d="M2 0l2 2.5-1.2 1.3a6 6 0 0 0 3.4 3.4L7.5 6 10 8l-1.5 2C4 10 0 6 0 1.5z"/></svg>
    <span>+1 555 010 0795</span>
    <svg width="8" height="6" viewBox="0 0 8 6"><rect class="icon-green" width="8" height="6"/><path d="M0 0l4 3 4-3" stroke="#fff" fill="none" stroke-width=".8"/></svg>
    <span>hello@standingmend.com</span>
  </div>
</header>

<nav class="abs nav">
  <a style="left:152px">Personal</a><span class="sep" style="left:193px"></span>
  <a style="left:238px">Business</a><span class="sep" style="left:280px"></span>
  <a style="left:322px">About us</a><span class="sep" style="left:367px"></span>
  <a style="left:422px">Account Login</a><span class="sep" style="left:475px"></span>
  <a style="left:517px">Sign Up</a>
</nav>

<section>
  <div class="abs hero" role="img" aria-label="Photo of business consultants in conversation, a smiling woman holding a tablet beside a senior colleague"></div>
  <h1 class="abs hero-title">Business Consulting</h1>
  <h2 class="abs hero-sub" style="font-weight:400">Cum sociis natoque penatibus</h2>
  <p class="abs hero-text">Vivamus porttitor purus nisi eleifend libero a tempus libero lectus feugiat felis Morbi diam mauris viverra gravida</p>
  <div class="abs dots"><span></span><span></span><span></span></div>
</section>

<section>
  <h2 class="abs welcome-title" style="font-weight:400">Welcome to Our Website Mainpage</h2>
  <div class="abs welcome-text">
    <p>Vivamus porttitor purus nisi eleifend libero a tempus libero lectus feugiat felis Morbi diam mauris viverra in gravida eu mattis in ante Morbi eget arcu Morbi porta libero id ullamcorper nonummy nibh ligula pulvinar metus eget consectetuer augue nisi quis lacus</p>
    <p>Curabitur iaculis tempus eros Curabitur vel mi sit amet magna malesuada ultrices Ut nisi erat fermentum vel congue id euismod in elit Fusce ultricies orci ac feugiat suscipit leo massa sodales velit et scelerisque mi tortor at ipsum cligula augue accumsan vestibulum ut commodo a mi Morbi ornare gravida elit Integer congue augue et malesuada iaculis ipsum dui aliquet felis at cursus magna nisl nec elit Praesent elementum elit at tellus</p>
  </div>
</section>

<section>
  <div class="abs services"></div>
  <h2 class="abs services-title" style="font-weight:400">Services We Provides</h2>

  <svg class="abs arrow" style="left:76px" width="10" height="32" viewBox="0 0 10 32"><path d="M9 1L1 16l8 15" stroke="#8a8a8a" fill="none"/></svg>
  <svg class="abs arrow" style="left:614px" width="10" height="32" viewBox="0 0 10 32"><path d="M1 1l8 15-8 15" stroke="#8a8a8a" fill="none"/></svg>

  <div class="abs service" style="left:98px">
    <svg width="28" height="24" viewBox="0 0 28 24"><rect x="9" y="1" width="10" height="5" rx="1" fill="none" stroke="#1a82f0" stroke-width="2"/><rect y="5" width="28" height="19" rx="2" fill="#1a82f0"/><rect x="0" y="12" width="28" height="1.5" fill="#fff"/><rect x="12" y="10" width="4" height="5" fill="#fff"/></svg>
    <h3>Business Reputation<br>Management</h3>
    <p>Cras a ante vitae enim iaculis aliquam Mauris nunc quam venenatis nec euismod sit amet egestas placerat est</p>
    <a>LEARN MORE</a>
  </div>
  <div class="abs service" style="left:227px">
    <svg width="28" height="24" viewBox="0 0 28 24"><rect width="28" height="18" rx="2" fill="#1a82f0"/><rect x="3" y="3" width="22" height="12" fill="#fff"/><rect x="11" y="18" width="6" height="4" fill="#1a82f0"/><rect x="7" y="22" width="14" height="2" fill="#1a82f0"/></svg>
    <h3>Reputation<br>Monitoring</h3>
    <p>Cras a ante vitae enim iaculis aliquam Mauris nunc quam venenatis nec euismod sit amet egestas placerat est</p>
    <a>LEARN MORE</a>
  </div>
  <div class="abs service" style="left:367px">
    <svg width="24" height="24" viewBox="0 0 24 24"><circle cx="12" cy="12" r="12" fill="#1a82f0"/><ellipse cx="12" cy="12" rx="5" ry="11" fill="none" stroke="#fff" stroke-width="1.2"/><path d="M1 12h22M3 6h18M3 18h18" stroke="#fff" stroke-width="1.2"/></svg>
    <h3>People Search<br>Site Removal</h3>
    <p>Cras a ante vitae enim iaculis aliquam Mauris nunc quam venenatis nec euismod sit amet egestas placerat est</p>
    <a>LEARN MORE</a>
  </div>
  <div class="abs service" style="left:497px">
    <svg width="24" height="24" viewBox="0 0 24 24"><path d="M11 2v11h11A11 11 0 1 1 11 2z" fill="#1a82f0"/><path d="M13 0a11 11 0 0 1 11 11H13z" fill="#1a82f0"/></svg>
    <h3>Arrest Record<br>Expungement</h3>
    <p>Cras a ante vitae enim iaculis aliquam Mauris nunc quam venenatis nec euismod sit amet egestas placerat est</p>
    <a>LEARN MORE</a>
  </div>
</section>

<section>
  <div class="abs signup"></div>
  <div class="abs signup-photo" role="img" aria-label="Photo of a smiling consultant in a light blue shirt with arms crossed"></div>
  <h2 class="abs signup-title" style="font-weight:400">Please Sign Up here</h2>
  <p class="abs signup-text">In massa libero interdum nec interdum vel blandit sed nulla In ullamcorper est eget tempor cursus neque mi consectetuer mi a ultricies massa est sed nisl Class aptent</p>
  <div class="abs field" style="left:118px;top:887px">First Name</div>
  <div class="abs field" style="left:229px;top:887px">Last Name</div>
  <div class="abs field" style="left:118px;top:907px">Email address</div>
  <div class="abs field" style="left:229px;top:907px">Phone</div>
  <div class="abs btn btn-green">Sign Up</div>
  <div class="abs or">or</div>
  <div class="abs btn btn-social">Sign Up with <i></i></div>
</section>

<footer>
  <div class="abs footer"></div>
  <div class="abs col" style="left:111px"><h4>COMPANY</h4><ul><li>Become A Partner</li><li>Company</li><li>FAQ'S</li><li>Our Team</li><li>Privacy Policy</li><li>TOS</li></ul></div>
  <span class="abs col-rule" style="left:192px"></span>
  <div class="abs col" style="left:217px"><h4>SERVICES</h4><ul><li>Personal Reputation</li><li>Business Reputation</li><li>Cheater Submission Removal</li><li>People Search Site Removal</li><li>Reputation Monitoring</li><li>Record Expungement</li></ul></div>
  <span class="abs col-rule" style="left:334px"></span>
  <div class="abs col" style="left:358px"><h4>RESOURCES</h4><ul><li>Case Studies</li><li>Free Reputation Check</li><li>Reputation Advice</li><li>Videos</li><li>Contact Us</li></ul></div>
  <span class="abs col-rule" style="left:454px"></span>
  <div class="abs col" style="left:481px"><h4>CONTACT INFO</h4><ul style="font-size:6.3px"><li style="line-height:10.5px">12-480 Larkmoor Avenue, Suite 210,<br>Fernvale, Ontario, Canada K0F 2B9</li><li>Phone: <b>+1 555 010 0795</b></li><li>Email: <b>hello@standingmend.com</b></li><li>www.StandingMend.com</li></ul></div>
  <div class="abs footer-social"><span></span><span></span><span></span><span></span></div>
  <div class="abs subfooter"><p>© 2015 Company Name All right reserved Term of Use</p></div>
</footer>

</body>
</html>
```